Business cards and Stationary for engineering design firm
Brask Industrial Advisory
Business cards and Stationary for engineering design firm - Engineering
Creative Brief
Professional
Dorian Pell
President
42 N 9th St Marlow, PA 17362
Dorian@BraskIndAdvisory.example
www.BraskIndAdvisory.example
We are looking for modern and professional looking business cards for an engineering firm that specializes in the electric utility industry. Subtle touches like abstract poles and wires on the business cards are welcomed. Use your imagination and have fun!
We are up for anything. Maybe just the company logo and the website address for the back.

```html
<!DOCTYPE html>
<html lang="en">
<head>
<meta charset="utf-8">
<title>Brask Industrial Advisory — Stationery</title>
<link rel="stylesheet" href="https://fonts.googleapis.com/css2?family=Cinzel:wght@500&family=Montserrat:wght@500&family=Open+Sans:wght@400;600&display=swap">
<style>
  :root {
    --navy: #24436e;
    --navy-deep: #16294a;
    --navy-light: #4f6f9c;
    --ink: #1f2a3a;
    --text: #4a5361;
    --paper: #ffffff;
    --backdrop: #f1f2f4;
    --line: #0d1420;
    --mist: #d9dee6;
  }
  html, body { margin: 0; padding: 0; overflow: hidden; }
  body { width: 1200px; height: 937px; background: var(--backdrop); position: relative; font-family: "Open Sans", sans-serif; }
  .piece { position: absolute; background: var(--paper); overflow: hidden; box-shadow: 0 2px 6px rgba(20,30,50,.18); }
  .wave { position: absolute; left: 0; bottom: 0; width: 100%; display: block; }
  .brand { text-align: center; color: var(--ink); }
  .brand-mark { display: block; margin: 0 auto; border-radius: 50%; background: var(--navy); }
  .brand-name { font-family: "Cinzel", serif; font-weight: 500; color: var(--ink); line-height: 1.05; margin: 0; letter-spacing: .02em; }
  .brand-tag { font-family: "Montserrat", sans-serif; font-weight: 500; color: var(--navy); text-transform: uppercase; letter-spacing: .14em; margin: 0; }
  .web { position: absolute; font-family: "Montserrat", sans-serif; color: #fff; letter-spacing: .12em; white-space: nowrap; }

  /* letterhead */
  .letterhead { left: 182px; top: 68px; width: 385px; height: 539px; }
  .letterhead .brand { margin-top: 24px; }
  .letterhead .brand-mark { width: 38px; height: 38px; margin-bottom: 6px; }
  .letterhead .brand-name { font-size: 17px; }
  .letterhead .brand-tag { font-size: 5.5px; margin-top: 3px; }
  .letter { position: absolute; left: 34px; top: 130px; width: 318px; font-size: 5.6px; line-height: 1.55; color: var(--text); }
  .letter p { margin: 0 0 7px; }
  .letter .signer { margin-top: 24px; }
  .letter .signer strong { font-weight: 600; color: var(--ink); }
  .contact { position: absolute; right: 24px; bottom: 18px; font-size: 5.4px; line-height: 1.8; color: #fff; text-align: left; white-space: nowrap; }
  .contact div { display: flex; align-items: center; gap: 4px; }
  .contact svg { width: 6px; height: 6px; fill: #fff; }

  /* presentation folder */
  .folder { left: 633px; top: 38px; width: 460px; height: 577px; }
  .folder .brand { margin-top: 212px; }
  .folder .brand-mark { width: 80px; height: 80px; margin-bottom: 12px; }
  .folder .brand-name { font-size: 31px; }
  .folder .brand-tag { font-size: 10px; margin-top: 6px; color: var(--ink); }
  .folder .web { right: 40px; bottom: 30px; font-size: 9.5px; }

  /* business cards */
  .card { width: 169px; height: 96px; left: 51px; }
  .card-front { top: 663px; }
  .card-front .brand { position: absolute; left: 6px; top: 6px; width: 108px; }
  .card-front .brand-mark { width: 14px; height: 14px; margin-bottom: 3px; }
  .card-front .brand-name { font-size: 5.8px; white-space: nowrap; }
  .card-front .brand-tag { font-size: 2.6px; margin-top: 2px; white-space: nowrap; letter-spacing: .1em; }
  .card-person { position: absolute; left: 16px; top: 40px; font-size: 4.2px; line-height: 1.5; color: var(--text); }
  .card-person strong { color: var(--ink); font-weight: 600; font-size: 5px; }
  .card-contact { position: absolute; right: 8px; bottom: 4px; font-size: 3.4px; line-height: 1.45; color: #fff; text-align: right; white-space: nowrap; }
  .card-back { top: 780px; height: 101px; }
  .card-back .brand { margin-top: 12px; }
  .card-back .brand-mark { width: 20px; height: 20px; margin-bottom: 4px; }
  .card-back .brand-name { font-size: 9.5px; white-space: nowrap; }
  .card-back .brand-tag { font-size: 3.2px; margin-top: 2px; }

  /* envelopes */
  .envelope-front { left: 266px; top: 671px; width: 430px; height: 210px; }
  .envelope-front .brand { position: absolute; left: 22px; top: 16px; width: 120px; }
  .envelope-front .brand-mark { width: 26px; height: 26px; margin-bottom: 4px; }
  .envelope-front .brand-name { font-size: 11px; }
  .envelope-front .brand-tag { font-size: 3.6px; margin-top: 2px; white-space: nowrap; }
  .envelope-front .faint-mark { position: absolute; right: 82px; top: 40px; width: 90px; height: 90px; border-radius: 50%; background: var(--mist); opacity: .6; }
  .envelope-front .web { left: 36px; bottom: 16px; font-size: 7px; }
  .envelope-back { left: 739px; top: 671px; width: 354px; height: 210px; }
  .envelope-back .web { left: 0; width: 100%; text-align: center; top: 46px; font-size: 8.5px; }
</style>
</head>
<body>

<!-- Letterhead -->
<section class="piece letterhead">
  <div class="brand">
    <span class="brand-mark"></span>
    <p class="brand-name">Brask Industrial Advisory</p>
    <p class="brand-tag">Electric Utility Design Solutions</p>
  </div>
  <div class="letter">
    <p>May 4, 2024</p>
    <p>Alder Grid Services<br>118 Quarry Rd, Lebanon, PA 17042</p>
    <p>Dear Ms. Hale,</p>
    <p>Thank you for the opportunity to support your distribution upgrade. Our team has reviewed the pole loading data, span lengths and conductor sizes, and we are ready to begin the detailed design phase next month.</p>
    <p>Attached is a summary of the proposed scope, schedule and staffing for each circuit.</p>
    <p>Please let us know if you would like to meet on site to walk the route before we issue drawings.</p>
    <p>Sincerely,</p>
    <p class="signer"><strong>Dorian Pell</strong><br>President</p>
  </div>
  <svg class="wave" viewBox="0 0 100 30" height="118" preserveAspectRatio="none" aria-hidden="true">
    <defs>
      <linearGradient id="lhBand" x1="0" y1="0" x2="1" y2="0">
        <stop offset="0" stop-color="#16294a"/><stop offset=".55" stop-color="#3a5a88"/><stop offset="1" stop-color="#24436e"/>
      </linearGradient>
    </defs>
    <path d="M0 8 C30 -1 60 20 100 2" fill="none" stroke="#d9dee6" stroke-width="1.2"/>
    <path d="M0 12 C30 3 60 22 100 6" fill="none" stroke="#0d1420" stroke-width=".7"/>
    <path d="M0 30 L0 15 C30 6 60 24 100 9 L100 30 Z" fill="url(#lhBand)"/>
  </svg>
  <div class="contact">
    <div><svg viewBox="0 0 10 10"><path d="M5 0a3.5 3.5 0 0 0-3.5 3.5C1.5 6 5 10 5 10s3.5-4 3.5-6.5A3.5 3.5 0 0 0 5 0zm0 5a1.5 1.5 0 1 1 0-3 1.5 1.5 0 0 1 0 3z"/></svg>42 N 9th St Marlow, PA 17362</div>
    <div><svg viewBox="0 0 10 10"><path d="M2 0l2 2.5-1 1.5a6 6 0 0 0 3 3l1.5-1L10 8l-1.5 2C4 10 0 6 0 1.5z"/></svg>(717) 555-0162</div>
    <div><svg viewBox="0 0 10 10"><path d="M0 2h10v6H0zM0 2l5 3.5L10 2" /></svg>Dorian@BraskIndAdvisory.example</div>
    <div><svg viewBox="0 0 10 10"><circle cx="5" cy="5" r="4.5"/></svg>www.BraskIndAdvisory.example</div>
  </div>
</section>

<!-- Presentation folder -->
<section class="piece folder">
  <div class="brand">
    <span class="brand-mark"></span>
    <p class="brand-name">Brask Industrial Advisory</p>
    <p class="brand-tag">Electric Utility Design Solutions</p>
  </div>
  <svg class="wave" viewBox="0 0 100 30" height="150" preserveAspectRatio="none" aria-hidden="true">
    <defs>
      <linearGradient id="fdBand" x1="0" y1="0" x2="1" y2="0">
        <stop offset="0" stop-color="#16294a"/><stop offset=".55" stop-color="#3a5a88"/><stop offset="1" stop-color="#24436e"/>
      </linearGradient>
    </defs>
    <path d="M0 6 C30 -2 60 18 100 1" fill="none" stroke="#d9dee6" stroke-width="1.2"/>
    <path d="M0 10 C30 2 60 21 100 5" fill="none" stroke="#0d1420" stroke-width=".6"/>
    <path d="M0 30 L0 13 C30 5 60 23 100 8 L100 30 Z" fill="url(#fdBand)"/>
  </svg>
  <div class="web">www.BraskIndAdvisory.example</div>
</section>

<!-- Business card front -->
<section class="piece card card-front">
  <div class="brand">
    <span class="brand-mark"></span>
    <p class="brand-name">Brask Industrial Advisory</p>
    <p class="brand-tag">Electric Utility Design Solutions</p>
  </div>
  <div class="card-person"><strong>Dorian Pell</strong><br>President</div>
  <svg class="wave" viewBox="0 0 100 30" height="40" preserveAspectRatio="none" aria-hidden="true">
    <defs>
      <linearGradient id="bcBand" x1="0" y1="0" x2="1" y2="0">
        <stop offset="0" stop-color="#16294a"/><stop offset=".55" stop-color="#3a5a88"/><stop offset="1" stop-color="#24436e"/>
      </linearGradient>
    </defs>
    <path d="M0 14 C30 4 60 20 100 4" fill="none" stroke="#0d1420" stroke-width=".8"/>
    <path d="M0 30 L0 18 C30 8 60 23 100 8 L100 30 Z" fill="url(#bcBand)"/>
  </svg>
  <div class="card-contact">42 N 9th St Marlow, PA 17362<br>Dorian@BraskIndAdvisory.example<br>www.BraskIndAdvisory.example</div>
</section>

<!-- Business card back -->
<section class="piece card card-back">
  <div class="brand">
    <span class="brand-mark"></span>
    <p class="brand-name">Brask Industrial Advisory</p>
    <p class="brand-tag">Electric Utility Design Solutions</p>
  </div>
  <svg class="wave" viewBox="0 0 100 30" height="22" preserveAspectRatio="none" aria-hidden="true">
    <path d="M0 12 C30 3 60 22 100 5" fill="none" stroke="#0d1420" stroke-width=".8"/>
    <path d="M0 30 L0 16 C30 7 60 25 100 9 L100 30 Z" fill="url(#bcBand)"/>
  </svg>
</section>

<!-- Envelope front -->
<section class="piece envelope-front">
  <div class="brand">
    <span class="brand-mark"></span>
    <p class="brand-name">Brask Industrial Advisory</p>
    <p class="brand-tag">Electric Utility Design Solutions</p>
  </div>
  <span class="faint-mark"></span>
  <svg class="wave" viewBox="0 0 100 30" height="72" preserveAspectRatio="none" aria-hidden="true">
    <defs>
      <linearGradient id="evBand" x1="0" y1="0" x2="1" y2="0">
        <stop offset="0" stop-color="#16294a"/><stop offset=".55" stop-color="#3a5a88"/><stop offset="1" stop-color="#24436e"/>
      </linearGradient>
    </defs>
    <path d="M0 6 C30 -2 60 18 100 2" fill="none" stroke="#d9dee6" stroke-width="1.2"/>
    <path d="M0 10 C30 2 60 21 100 6" fill="none" stroke="#0d1420" stroke-width=".6"/>
    <path d="M0 30 L0 14 C30 5 60 24 100 9 L100 30 Z" fill="url(#evBand)"/>
  </svg>
  <div class="web">www.BraskIndAdvisory.example</div>
</section>

<!-- Envelope back -->
<section class="piece envelope-back">
  <svg viewBox="0 0 354 210" width="354" height="210" aria-hidden="true" style="position:absolute;left:0;top:0">
    <defs>
      <linearGradient id="flap" x1="0" y1="0" x2="1" y2="0">
        <stop offset="0" stop-color="#16294a"/><stop offset=".5" stop-color="#4f6f9c"/><stop offset="1" stop-color="#24436e"/>
      </linearGradient>
    </defs>
    <path d="M0 0 H354 V62 C300 88 230 104 177 104 C124 104 54 88 0 62 Z" fill="url(#flap)"/>
    <path d="M0 66 C54 92 124 108 177 108 C230 108 300 92 354 66" fill="none" stroke="#0d1420" stroke-width="1"/>
  </svg>
  <div class="web">www.BraskIndAdvisory.example</div>
</section>

</body>
</html>
```